Optical shop needs a signage that attracts families such as parents and kids

My shop name is Miro optical. I need a signage for my optical shop that can attract families, targeting mainly kids and their adults. My shop is situated in neighborhood areas and sells affordable spectacles. The interior of my shop is clean and white base, very comfortable feeling that makes people feel like they have come home. Signage should not be too fancy and colourful. I have attached a mascot for my signage too, it is a cat that wear spectacles. You can either use or don't use the mascot for the design. Let me view your creative side. :)

The theme would be more of Japanese. Please do something that has Japanese style or elements for the signage logo design. Colours used can be more of Japanese origin.
Updates

Project Deadline Extended
Reason: There are not enough designs to choose from. Please help to send in more designs. Thanks.

The theme would be more Japanese style as people would like to associate my shop name with it.

Target Market(s)

Families, teens and elderly

Industry/Entity Type

Shop

Font styles to use
Script

```html
<!DOCTYPE html>
<html lang="en">
<head>
<meta charset="utf-8">
<title>Miro Optical Signage</title>
<link rel="stylesheet" href="https://fonts.googleapis.com/css2?family=Pinyon+Script&display=swap">
<style>
  :root {
    --sky-light: #2aa6e3;
    --sky-mid: #1e8fd6;
    --sky-deep: #1a6cbf;
    --name-white: #ffffff;
    --mascot-white: #fbfbfb;
    --mascot-shade: #dfe7ee;
  }
  html, body {
    margin: 0;
    padding: 0;
    width: 1200px;
    height: 309px;
    overflow: hidden;
    background: #ffffff;
  }
  .signage {
    position: relative;
    width: 1200px;
    height: 309px;
    overflow: hidden;
    background: linear-gradient(90deg, var(--sky-light) 0%, var(--sky-mid) 50%, var(--sky-deep) 100%);
  }
  .signage__mascot {
    position: absolute;
    left: 40px;
    top: 36px;
    width: 198px;
    height: 234px;
  }
  .signage__name {
    position: absolute;
    left: 292px;
    top: 30px;
    width: 860px;
    margin: 0;
    font-family: "Pinyon Script", cursive;
    font-weight: 400;
    font-style: normal;
    font-size: 158px;
    line-height: 1.4;
    color: var(--name-white);
    white-space: nowrap;
    letter-spacing: 2px;
  }
</style>
</head>
<body>
  <div class="signage">
    <svg class="signage__mascot" viewBox="0 0 198 234" role="img" aria-label="Mascot illustration area">
      <defs>
        <linearGradient id="mascot-fill" x1="0" y1="0" x2="1" y2="1">
          <stop offset="0" stop-color="#fbfbfb"/>
          <stop offset="1" stop-color="#dfe7ee"/>
        </linearGradient>
      </defs>
      <rect x="0" y="0" width="198" height="234" rx="60" fill="url(#mascot-fill)"/>
    </svg>
    <h1 class="signage__name">Miro Optical</h1>
  </div>
</body>
</html>
```